Business Card for Concrete supplier
Oak Lane Ready Mix
Business Card for Concrete supplier - Construction
Creative Brief
Simple
Marcel Dunham Jr.
President
P.O. Box 5172 Pearland, TX 77514
oaklanereadymix@mailnest.example
http://oaklanereadymix.example

```html
<!DOCTYPE html>
<html lang="en">
<head>
<meta charset="utf-8">
<title>Oak Lane Ready Mix — Business Card</title>
<link rel="stylesheet" href="https://fonts.googleapis.com/css2?family=Roboto+Condensed:wght@400;700&family=Roboto:wght@400;500&display=swap">
<style>
  :root {
    --page-bg: #e4e4e6;
    --card-bg: #ffffff;
    --logo-grey: #8a8a8c;
    --brand-blue: #1f3f9a;
    --brand-red: #d0202a;
    --text-dark: #2a2a2e;
    --text-muted: #8d8d90;
  }
  * { margin: 0; padding: 0; box-sizing: border-box; }
  html, body { width: 1200px; height: 901px; overflow: hidden; }
  body {
    background: var(--page-bg);
    font-family: "Roboto", Arial, sans-serif;
    display: flex;
    flex-direction: column;
    align-items: center;
    justify-content: center;
    gap: 56px;
  }
  .card {
    position: relative;
    width: 600px;
    height: 343px;
    background: var(--card-bg);
    border-radius: 14px;
    box-shadow: 0 8px 24px rgba(0,0,0,0.18);
  }
  .card--front {
    display: flex;
    flex-direction: column;
    align-items: center;
    justify-content: center;
  }
  .front-wordmark {
    font-family: "Roboto Condensed", Arial, sans-serif;
    font-weight: 700;
    font-size: 54px;
    letter-spacing: 1px;
    text-transform: uppercase;
    color: var(--logo-grey);
    white-space: nowrap;
  }
  .front-website {
    margin-top: 10px;
    font-size: 13px;
    letter-spacing: 0.5px;
    color: var(--text-muted);
  }
  .back-wordmark {
    position: absolute;
    left: 40px;
    top: 52px;
    font-family: "Roboto Condensed", Arial, sans-serif;
    font-weight: 700;
    font-size: 30px;
    text-transform: uppercase;
    color: var(--brand-blue);
    white-space: nowrap;
  }
  .person {
    position: absolute;
    right: 40px;
    top: 46px;
    text-align: right;
  }
  .person-name {
    font-family: "Roboto Condensed", Arial, sans-serif;
    font-weight: 700;
    font-size: 20px;
    color: var(--brand-blue);
    white-space: nowrap;
  }
  .person-title {
    margin-top: 2px;
    font-size: 12px;
    color: var(--text-dark);
  }
  .rule {
    position: absolute;
    left: 40px;
    right: 40px;
    top: 96px;
    height: 2px;
    background: var(--brand-red);
  }
  .address {
    position: absolute;
    right: 40px;
    top: 120px;
    text-align: right;
    font-size: 13px;
    line-height: 1.45;
    color: var(--text-dark);
  }
  .contact-rule {
    position: absolute;
    left: 40px;
    right: 40px;
    top: 218px;
    height: 2px;
    background: var(--brand-red);
  }
  .contact-list {
    position: absolute;
    left: 40px;
    top: 230px;
    list-style: none;
  }
  .contact-item {
    display: flex;
    align-items: center;
    gap: 10px;
    height: 22px;
    font-size: 13px;
    color: var(--text-dark);
    white-space: nowrap;
  }
  .contact-icon { width: 15px; height: 15px; flex: none; }
</style>
</head>
<body>
  <section class="card card--front" aria-label="Card front">
    <div class="front-wordmark">Oak Lane Ready Mix</div>
    <div class="front-website">www.oaklanereadymix.example</div>
  </section>

  <section class="card card--back" aria-label="Card back">
    <div class="back-wordmark">Oak Lane Ready Mix</div>
    <div class="person">
      <div class="person-name">Marcel Dunham Jr.</div>
      <div class="person-title">President</div>
    </div>
    <div class="rule"></div>
    <div class="address">P.O. Box 5172<br>Harlow Ridge, HR 77514</div>
    <div class="contact-rule"></div>
    <ul class="contact-list">
      <li class="contact-item">
        <svg class="contact-icon" viewBox="0 0 16 16"><rect width="16" height="16" rx="2" fill="#1f3f9a"/><path d="M5 3.5 L6.8 3.5 L7.4 6 L6.3 7 Q7.3 9 9 9.7 L10 8.6 L12.5 9.2 L12.5 11 Q12.5 12.5 11 12.5 Q4 12 3.5 5 Q3.5 3.5 5 3.5Z" fill="#fff"/></svg>
        (713) 555-0148
      </li>
      <li class="contact-item">
        <svg class="contact-icon" viewBox="0 0 16 16"><rect width="16" height="16" rx="2" fill="#1f3f9a"/><rect x="5" y="3" width="6" height="10" rx="1" fill="#fff"/><rect x="6" y="4.5" width="4" height="6" fill="#1f3f9a"/></svg>
        (281) 555-0172
      </li>
      <li class="contact-item">
        <svg class="contact-icon" viewBox="0 0 16 16"><rect width="16" height="16" rx="2" fill="#1f3f9a"/><rect x="3" y="4.5" width="10" height="7" fill="#fff"/><path d="M3 4.5 L8 8.5 L13 4.5" fill="none" stroke="#1f3f9a" stroke-width="1"/></svg>
        oaklanereadymix@mailnest.example
      </li>
      <li class="contact-item">
        <svg class="contact-icon" viewBox="0 0 16 16"><rect width="16" height="16" rx="2" fill="#1f3f9a"/><circle cx="8" cy="8" r="4.5" fill="none" stroke="#fff" stroke-width="1.2"/><path d="M3.5 8 H12.5 M8 3.5 Q5.5 8 8 12.5 M8 3.5 Q10.5 8 8 12.5" fill="none" stroke="#fff" stroke-width="1"/></svg>
        www.oaklanereadymix.example
      </li>
    </ul>
  </section>
</body>
</html>
```